north lark upkeep services

Target Market(s)

General letter head for emails and letter quotes ect

Colors
0054AA
0677BA
7BADD7
CADEEF
E8F1F8
0094D4
00A9DD
6FCCEA
C7EBF8
E9F6FB

Requirements
Must have
• logo phone email website names
Nice to have
• what we do (from the website)

```html
<!DOCTYPE html>
<html lang="en">
<head>
<meta charset="utf-8">
<title>North Lark Upkeep Services — Letterhead</title>
<link href="https://fonts.googleapis.com/css2?family=Poppins:wght@400;700&display=swap" rel="stylesheet">
<style>
  :root {
    --navy: #0054AA;
    --blue: #0677BA;
    --sky: #0094D4;
    --mist: #E8F1F8;
    --ink: #1d1d1f;
    --paper: #ffffff;
    --backdrop: #c9c9c9;
  }
  html, body {
    margin: 0;
    width: 1200px;
    height: 686px;
    overflow: hidden;
    background: var(--backdrop);
    font-family: "Poppins", sans-serif;
  }
  .letterhead {
    position: absolute;
    left: 365px;
    top: 39px;
    width: 470px;
    height: 608px;
    background: var(--paper);
    box-shadow: 0 6px 18px rgba(0,0,0,0.18);
    overflow: hidden;
  }
  .brand {
    position: absolute;
    left: 36px;
    top: 34px;
    display: flex;
    align-items: center;
    gap: 10px;
  }
  .brand-dot {
    width: 30px;
    height: 30px;
    border-radius: 50%;
    background: var(--sky);
  }
  .brand-name {
    font-weight: 700;
    font-size: 13px;
    line-height: 1.15;
    color: var(--navy);
    text-transform: uppercase;
    letter-spacing: 0.04em;
    width: 120px;
  }
  .backdrop-disc {
    position: absolute;
    left: 105px;
    top: 150px;
    width: 260px;
    height: 260px;
    border-radius: 50%;
    background: var(--mist);
    opacity: 0.7;
  }
  .footer {
    position: absolute;
    left: 36px;
    right: 36px;
    bottom: 26px;
  }
  .footer-rule {
    height: 1.5px;
    background: var(--blue);
    margin-bottom: 10px;
  }
  .contact-row {
    display: flex;
    justify-content: space-between;
    align-items: center;
    font-size: 9.5px;
    color: var(--ink);
    margin-top: 6px;
  }
  .contact-row.address { justify-content: flex-start; }
  .contact-item { display: flex; align-items: center; gap: 5px; }
  .contact-item svg { width: 10px; height: 10px; fill: var(--sky); flex: none; }
</style>
</head>
<body>
  <main class="letterhead">
    <header class="brand">
      <span class="brand-dot"></span>
      <span class="brand-name">North Lark Upkeep Services</span>
    </header>

    <div class="backdrop-disc" aria-hidden="true"></div>

    <footer class="footer">
      <div class="footer-rule"></div>
      <div class="contact-row address">
        <span class="contact-item">
          <svg viewBox="0 0 10 10"><path d="M5 0a3.5 3.5 0 0 0-3.5 3.5C1.5 6 5 10 5 10s3.5-4 3.5-6.5A3.5 3.5 0 0 0 5 0zm0 5a1.5 1.5 0 1 1 0-3 1.5 1.5 0 0 1 0 3z"/></svg>
          418 Alder Bend Rd. Suite 120, Dallas, TX 75201
        </span>
      </div>
      <div class="contact-row">
        <span class="contact-item">
          <svg viewBox="0 0 10 10"><path d="M2 0.5l2 2-1 1.2c.6 1.3 1.6 2.3 2.8 2.8L7 5.5l2 2-1.2 1.8C4 9 1 6 .3 1.7z"/></svg>
          (555) 214-0386
        </span>
        <span class="contact-item">
          <svg viewBox="0 0 10 10"><path d="M0 2h10v6H0zM.6 2.5 5 5.6l4.4-3.1v.9L5 6.5.6 3.4z"/></svg>
          hello@northlarkupkeep.com
        </span>
        <span class="contact-item">
          <svg viewBox="0 0 10 10"><circle cx="5" cy="5" r="5"/></svg>
          www.northlarkupkeep.com
        </span>
      </div>
    </footer>
  </main>
</body>
</html>
```